Movie Poster Design for the Independent documentary, BEYOND NINE

We are seeking a compelling and provocative poster design for our first independent film, Beyond Nine. This is the story of Mason Fellick, a relentlessly positive young man facing the last year of his life after 7 years of living with a rare and incurable cancer, osteosarcoma. We need to take this poster with us to Brightwater next week where we can share our story with potential distributors and industry executives. We have applied to other festivals this is the first of the season and we hope to be selected for others.

Mason Fellick is an inspiration to almost anyone he meets, he's charming, funny, human and a generous soul who does what ever he can to help the next guy or the next kid. Mason wants pediatric cancer to stop with him and he does all he can with his days to do that and still have fun and enjoy life. We can all learn a lot from Mason. Be sure to watch our trailer, like us on Chatterly and give us an amazing design! Many images of Mason are available for download on our website. www.beyondnine-film.org - we also had a Fundmoor campaign and there are images there too. We've liked MG_7107.jpg best for promotional pieces so far.

We have used an image of Mason for postcards that feels similar to the image of "The Woman by the Lantern" and some on our team like it's simplicity but that design can be enhanced too. As the co-director I am open, I really want to see some fresh creativity on this and so I invite you to submit your best work.

One small note, Mason loves orange and we do to so if you can weave that in somehow that would be awesome. If you prefer to work with high rez images email me and I will send you a link to our full rez images.

As for poster text here is what we have written and some links to look at

BEYOND NINE Poster

http://www.layoutharbor.net/2011/02/7-elements-of-a-great-movie-poster-design/

Beyond Nine – Poster credits – one sheet size 27" × 40" and scalable to 7 x 11

Title - Beyond Nine

Chose a tag line

"It’s all about perspective"

"What would you do with the last year of your life?"

"Never, never give up"

---------------------
MOVIE POSTER FONT for credits
Steel Tong font - http://www.quillbarn4.net/2009/12/the-movie-poster-font-you-were-looking-for/

Larger Font

A Delvane Production
A film by co-directors
Rosalind Techter
Noor Delvane

Produced by
Noor Delvane
Rosalind Techter

Smaller font
Co Produced by

Tarik Bel-Haddou
Samir Bel-Haddou
Pruett Family
Walter Brindle
Marcia Brindle
Al Brindle
Nadine Brindle
Lavanya Osei
Herbert J. Vossel
Colette Vossel
Tammy Corvell
Greg Corvell
Wendling Family
Morgan Dalquist
Nathaniel Dalquist

Written by
Mason T. Fellick
Rosalind Techter

Directors of Photography

Benjamin Thorvald
Daniel Pemberlin

Editor
Daniel Pemberlin
Ilse Varno

Production Associate
Rob Kettleby

Original Music
Paul Marcovich

Larger font
Coming Soon
Or
Watch this with someone you love

*we know we have alot of co producers names, one option might be to cut them or to find a creative way to deal with them all.

Thank you and happy creating!
The Beyond Nine Team

Target Market(s)

Young adults and families

Industry/Entity Type

Industry

Font styles to use
Serif
Other font styles liked:
• open to suggestions

Colors
3176b5
faa54c
f79020
cfdeed
919191
7f7f7f
000000
333333
d3d3d3

Requirements
Must have
• Positivity and feel real and authentic
Nice to have
• some enhancements
Should not have
• should not be sleek, high tech or all graphics

```html
<!DOCTYPE html>
<html lang="en">
<head>
<meta charset="utf-8">
<title>Beyond Nine — Poster</title>
<link rel="stylesheet" href="https://fonts.googleapis.com/css2?family=Raleway:wght@200;300&family=Montserrat:wght@200;900&family=Oswald:wght@300;400;500&display=swap">
<style>
  :root {
    --backdrop: #e9e7e3;
    --orange: #f79020;
    --orange-soft: #faa54c;
    --white: #ffffff;
    --ink: #1c1512;
    --credit: #d3d3d3;
    --skin-light: #b5826f;
    --skin-mid: #7d5243;
    --skin-deep: #3a2620;
    --shadow: #120c0a;
  }
  * { box-sizing: border-box; margin: 0; padding: 0; }
  html, body { width: 1200px; height: 1148px; overflow: hidden; background: var(--backdrop); }
  .poster {
    position: absolute; left: 250px; top: 49px; width: 700px; height: 1050px;
    overflow: hidden; background: var(--shadow);
  }
  .poster__photo {
    position: absolute; inset: 0;
    background:
      radial-gradient(ellipse 48% 55% at 50% 52%, var(--skin-light) 0%, var(--skin-mid) 45%, var(--skin-deep) 78%, var(--shadow) 100%);
  }
  .poster__shade {
    position: absolute; inset: 0;
    background: linear-gradient(180deg, rgba(20,12,10,.35) 0%, rgba(20,12,10,.1) 40%, rgba(20,12,10,.35) 70%, rgba(20,12,10,.75) 100%);
  }
  .tagline {
    position: absolute; left: 0; width: 100%;
    font-family: "Raleway", sans-serif; font-weight: 200; color: var(--orange);
    font-size: 122px; line-height: 1; text-align: center; text-transform: uppercase;
  }
  .tagline--wide { letter-spacing: 0.36em; padding-left: 0.36em; }
  .tagline--one { top: 80px; }
  .tagline--two { top: 254px; }
  .tagline--three { top: 415px; font-size: 118px; letter-spacing: -0.01em; }
  .title {
    position: absolute; left: 0; width: 100%; top: 600px;
    text-align: center; color: var(--white); line-height: 1; white-space: nowrap;
  }
  .title__bold { font-family: "Montserrat", sans-serif; font-weight: 900; font-size: 84px; letter-spacing: -0.04em; }
  .title__thin { font-family: "Montserrat", sans-serif; font-weight: 200; font-size: 84px; letter-spacing: -0.03em; }
  .banner { position: absolute; left: 205px; top: 732px; width: 290px; height: 50px; }
  .banner__text {
    position: absolute; inset: 0; display: flex; align-items: center; justify-content: center;
    font-family: "Oswald", sans-serif; font-weight: 400; font-size: 18px; letter-spacing: .04em;
    color: var(--credit); text-transform: uppercase;
  }
  .credits {
    position: absolute; left: 110px; width: 480px; top: 790px;
    font-family: "Oswald", sans-serif; text-transform: uppercase; text-align: center; color: var(--credit);
  }
  .credits__lead { font-size: 19px; font-weight: 500; line-height: 1.15; letter-spacing: .01em; }
  .credits__rule { border-top: 1px solid var(--credit); margin: 6px 0 3px; opacity: .8; }
  .credits__label { font-size: 7px; letter-spacing: .1em; }
  .credits__names { font-size: 9.5px; font-weight: 400; line-height: 1.45; letter-spacing: .02em; }
  .credits__crew { font-size: 7.5px; line-height: 1.5; margin-top: 8px; letter-spacing: .02em; }
  .credits__role { color: var(--orange); }
  .release {
    position: absolute; left: 0; width: 100%; top: 952px; text-align: center;
    font-family: "Oswald", sans-serif; font-weight: 300; font-size: 44px; letter-spacing: .28em;
    text-transform: uppercase; color: var(--white);
  }
  .release__accent { color: var(--orange); }
</style>
</head>
<body>
  <main class="poster">
    <div class="poster__photo" role="img" aria-label="Close-up portrait photograph of Mason smiling, filling the whole poster in warm skin tones"></div>
    <div class="poster__shade"></div>

    <p class="tagline tagline--wide tagline--one">Never</p>
    <p class="tagline tagline--wide tagline--two">Never</p>
    <p class="tagline tagline--three">Give Up</p>

    <h1 class="title"><span class="title__bold">BEYOND</span><span class="title__thin">NINE</span></h1>

    <div class="banner">
      <svg width="290" height="50" viewBox="0 0 290 50" aria-hidden="true">
        <polygon points="0,14 26,14 26,44 0,44 10,29" fill="#1c1512"/>
        <polygon points="290,14 264,14 264,44 290,44 280,29" fill="#1c1512"/>
        <rect x="20" y="6" width="250" height="32" fill="#241b17" stroke="#7f7f7f" stroke-width="1"/>
      </svg>
      <span class="banner__text">A Delvane Production</span>
    </div>

    <section class="credits">
      <p class="credits__lead">A film by co-directors : Rosalind Techter , Noor Delvane</p>
      <p class="credits__lead">Produced by : Noor Delvane, Rosalind Techter</p>
      <div class="credits__rule"></div>
      <p class="credits__label">Co-produced by</p>
      <p class="credits__names">
        Tarik Bel-Haddou · Samir Bel-Haddou · Pruett Family · Walter Brindle · Marcia Brindle · Al Brindle<br>
        Nadine Brindle · Lavanya Osei · Herbert J. Vossel · Colette Vossel · Tammy Corvell · Greg Corvell<br>
        Wendling Family · Morgan Dalquist · Nathaniel Dalquist
      </p>
      <p class="credits__crew">
        <span class="credits__role">Written by</span> Mason T. Fellick, Rosalind Techter
        <span class="credits__role">Directors of Photography</span> Benjamin Thorvald · Daniel Pemberlin<br>
        <span class="credits__role">Editor</span> Daniel Pemberlin · Ilse Varno
        <span class="credits__role">Production Associate</span> Rob Kettleby
        <span class="credits__role">Original Music</span> Paul Marcovich
      </p>
    </section>

    <p class="release">Coming <span class="release__accent">Soon</span></p>
  </main>
</body>
</html>
```